Solar Billboard Design

We require a billboard 24ftx10ft in size for our solar company.
Artwork Requirement’s:
• Sent on PDF file
• At least 300 dpi
• Scaled to 25% of banner size (24ft x 10ft)
• Please allow at least 40mm space from the artwork edge to allow for any hems and eyelets. This will ensure any important text/images are not cropped/overlapped.
The billboard must have on it:
Solar & Battery Packages
From £8750
In Stock Now!
brightfieldpower.co.uk (must stand out)
________________________
I have attached our logo and some images. I'm not sure if they are good enough quality so you may need to use a stock image.
Kind regards,
Marcus
Target Market(s)
Men & Women aged 35-70, homeowners
Industry/Entity Type
Solar / Construction
Look and feel
Each slider illustrates characteristics of the customer's brand and the style your logo design should communicate.

```html
<!DOCTYPE html>
<html lang="en">
<head>
<meta charset="utf-8">
<title>Solar &amp; Battery Packages Billboard</title>
<link rel="stylesheet" href="https://fonts.googleapis.com/css2?family=Anton&family=Montserrat:wght@500;600;800&display=swap">
<style>
  :root {
    --stage: #403c3d;
    --green: #2cc15d;
    --green-deep: #17883d;
    --navy: #1f2430;
    --white: #ffffff;
    --charcoal: #3d3a3b;
    --ink: #1d1d1d;
    --logo-grey: #3b3b3d;
    --sky: #4f7fc0;
    --roof: #e07a45;
    --panel: #2a3f6e;
    --wall: #f2ede6;
  }
  html, body {
    margin: 0;
    width: 1200px;
    height: 1200px;
    overflow: hidden;
    background: var(--stage);
  }
  .billboard {
    position: absolute;
    left: 50px;
    top: 371px;
    width: 1100px;
    height: 458px;
    display: block;
  }
  .headline { font-family: "Montserrat", sans-serif; font-weight: 600; font-size: 61px; fill: var(--white); }
  .price { font-family: "Anton", sans-serif; font-size: 118px; fill: var(--green); stroke: var(--white); stroke-width: 4px; paint-order: stroke; }
  .stock { font-family: "Montserrat", sans-serif; font-weight: 800; font-size: 56px; fill: var(--green); }
  .web-address { font-family: "Montserrat", sans-serif; font-weight: 800; font-size: 38px; fill: var(--ink); }
  .brand-name { font-family: "Montserrat", sans-serif; font-weight: 500; font-size: 19px; letter-spacing: 2px; fill: var(--logo-grey); }
</style>
</head>
<body>
<svg class="billboard" viewBox="0 0 1100 458" xmlns="http://www.w3.org/2000/svg">
  <defs>
    <linearGradient id="house-photo" x1="0" y1="0" x2="0" y2="1">
      <stop offset="0" stop-color="var(--sky)"/>
      <stop offset="0.22" stop-color="var(--sky)"/>
      <stop offset="0.27" stop-color="var(--roof)"/>
      <stop offset="0.36" stop-color="var(--panel)"/>
      <stop offset="0.58" stop-color="var(--panel)"/>
      <stop offset="0.63" stop-color="var(--roof)"/>
      <stop offset="0.72" stop-color="var(--wall)"/>
      <stop offset="1" stop-color="var(--wall)"/>
    </linearGradient>
    <linearGradient id="header-band" x1="0" y1="0" x2="0" y2="1">
      <stop offset="0" stop-color="var(--green-deep)"/>
      <stop offset="1" stop-color="var(--green)"/>
    </linearGradient>
  </defs>

  <rect class="house-photo" role="img" aria-label="Photo of a house roof with solar panels under a blue sky" x="0" y="0" width="1100" height="458" fill="url(#house-photo)"/>

  <polygon class="offer-panel" points="61,0 777,0 634,458 0,458 0,183" fill="var(--white)"/>
  <polygon class="corner-strip" points="0,0 61,0 0,183" fill="var(--navy)"/>
  <polygon class="edge-strip" points="61,0 96,0 0,307 0,183" fill="var(--green)"/>
  <polygon class="header-band" points="96,0 749,0 705,141 54,141" fill="url(#header-band)"/>
  <polygon class="url-bar" points="0,369 653,369 625,458 0,458" fill="var(--green)"/>

  <text class="headline" x="104" y="68">SOLAR &amp; BATTERY</text>
  <text class="headline" x="104" y="127">PACKAGES</text>

  <text class="price" x="45" y="260" textLength="612" lengthAdjust="spacingAndGlyphs">FROM £8750</text>

  <rect class="stock-box" x="42" y="273" width="499" height="61" fill="var(--charcoal)"/>
  <text class="stock" x="50" y="325" textLength="475" lengthAdjust="spacingAndGlyphs">IN STOCK NOW!</text>

  <g class="globe-icon" fill="none" stroke="var(--white)" stroke-width="2">
    <circle cx="46" cy="415" r="17"/>
    <ellipse cx="46" cy="415" rx="7" ry="17"/>
    <line x1="29" y1="415" x2="63" y2="415"/>
    <line x1="32" y1="405" x2="60" y2="405"/>
    <line x1="32" y1="425" x2="60" y2="425"/>
  </g>
  <text class="web-address" x="80" y="429" textLength="530" lengthAdjust="spacingAndGlyphs">www.brightfieldpower.co.uk</text>

  <rect class="brand-mark" x="852" y="378" width="40" height="40" fill="var(--green)"/>
  <text class="brand-name" x="906" y="375">BRIGHTFIELD</text>
  <text class="brand-name" x="906" y="406">ENERGY</text>
  <text class="brand-name" x="906" y="437">GROUP</text>
</svg>
</body>
</html>
```